I need a clean and unique business card

On one side I want it will have the company name and logo with the text underneath "The Next Measure"
The other side will have my contact information:
Miles Dorran
Visionary & Founder
miles.dorran@velomedix.com
1.800.417.2968
The logo can get grayed out in a rotated angle.
Use your creativity for other examples

```html
<!DOCTYPE html>
<html lang="en">
<head>
<meta charset="utf-8">
<title>Orvello Care Business Card</title>
<link href="https://fonts.googleapis.com/css2?family=Open+Sans:wght@600&family=Quicksand:wght@500;600&display=swap" rel="stylesheet">
<style>
  :root {
    --stage: #232325;
    --card-black: #0b0b0c;
    --card-white: #ffffff;
    --brand-blue: #3a86cf;
    --brand-teal: #2bbfa4;
    --brand-sky: #4cb3e3;
    --brand-navy: #2a74bd;
    --ink: #2b2b2b;
  }
  * { box-sizing: border-box; margin: 0; padding: 0; }
  html, body { width: 1200px; height: 900px; overflow: hidden; }
  body {
    background: var(--stage);
    position: relative;
    font-family: "Quicksand", "Open Sans", sans-serif;
  }
  .card {
    position: absolute;
    width: 560px;
    height: 320px;
    border-radius: 26px;
    overflow: hidden;
  }
  /* Front */
  .card--front {
    left: 70px;
    top: 80px;
    background: var(--card-black);
    display: flex;
    flex-direction: column;
    align-items: center;
    justify-content: center;
  }
  .brand {
    display: flex;
    align-items: center;
    gap: 14px;
  }
  .brand__mark {
    width: 22px;
    height: 22px;
    background: var(--brand-teal);
  }
  .brand__name {
    font-family: "Open Sans", sans-serif;
    font-weight: 600;
    font-size: 44px;
    color: var(--brand-blue);
    letter-spacing: 0.5px;
    white-space: nowrap;
  }
  .brand__tagline {
    margin-top: 4px;
    font-family: "Quicksand", sans-serif;
    font-weight: 600;
    font-size: 15px;
    letter-spacing: 4px;
    color: var(--brand-teal);
  }
  /* Back */
  .card--back {
    left: 570px;
    top: 500px;
    background: var(--card-white);
    padding: 70px 0 0 44px;
  }
  .accent-band {
    position: absolute;
    right: 0;
    top: 0;
    width: 150px;
    height: 100%;
  }
  .contact__name {
    font-size: 24px;
    font-weight: 600;
    color: var(--brand-teal);
    letter-spacing: 0.5px;
    text-transform: uppercase;
  }
  .contact__title {
    font-size: 15px;
    font-weight: 500;
    color: var(--ink);
    margin-top: 2px;
  }
  .contact__address {
    margin-top: 28px;
    font-size: 14px;
    line-height: 1.35;
    color: var(--ink);
  }
  .contact__list {
    list-style: none;
    margin-top: 12px;
    font-size: 15px;
    color: var(--ink);
  }
  .contact__list li {
    display: flex;
    align-items: center;
    gap: 12px;
    margin-bottom: 5px;
  }
  .contact__list svg { width: 16px; height: 16px; flex: none; }
  .web-highlight { color: var(--brand-teal); }
</style>
</head>
<body>
  <section class="card card--front">
    <div class="brand">
      <span class="brand__mark"></span>
      <span class="brand__name">Orvello Care</span>
    </div>
    <div class="brand__tagline">The Next Measure</div>
  </section>

  <section class="card card--back">
    <svg class="accent-band" viewBox="0 0 150 320" preserveAspectRatio="none" aria-hidden="true">
      <defs>
        <linearGradient id="bandGradient" x1="0" y1="0" x2="0" y2="1">
          <stop offset="0" stop-color="#2bbfa4"/>
          <stop offset="1" stop-color="#2a74bd"/>
        </linearGradient>
      </defs>
      <rect x="90" y="0" width="60" height="320" fill="url(#bandGradient)"/>
    </svg>

    <h1 class="contact__name">Miles Dorran</h1>
    <p class="contact__title">Visionary &amp; Founder</p>
    <p class="contact__address">Northgate , 4120 Linden Park,<br>Suite #12-40, Austin, Texas 78701</p>
    <ul class="contact__list">
      <li>
        <svg viewBox="0 0 16 16" aria-hidden="true"><path d="M3 6c0-2 2-3 5-3s5 1 5 3v1h-3V6H6v1H3z M4 8h8l1 5H3z" fill="#2bbfa4"/></svg>
        1.800.417.2968
      </li>
      <li>
        <svg viewBox="0 0 16 16" aria-hidden="true"><path d="M14 2 2 7l5 2 2 5z" fill="#3a86cf"/></svg>
        miles.dorran@velomedix.com
      </li>
      <li>
        <svg viewBox="0 0 16 16" aria-hidden="true"><circle cx="8" cy="8" r="6" fill="none" stroke="#2a74bd" stroke-width="1.6"/><path d="M2 8h12M8 2c-3 3-3 9 0 12M8 2c3 3 3 9 0 12" fill="none" stroke="#2a74bd" stroke-width="1.2"/></svg>
        <span>www.<span class="web-highlight">orvellocare</span>.com</span>
      </li>
    </ul>
  </section>
</body>
</html>
```